Motion Harbor 21-Day Detox

We need a flyer that we can use to post up in our gym and in some pagebook marketing that will help us promote a 21-day detox promo we are doing. Will need a .pdf and .jpg version.

We have a fitness studio, in Napa, CA. Most clients are already in a monthly membership that provides fitness but we like to do occasional short term programs that enhance and accelerate their results. This program will focus on nutrition and the support and accountability of a group.

Target Market(s)

Mostly women in their 40's who want to move better, look better and feel better by living a healthier lifestyle through exercise and nutrition.

Industry/Entity Type

Fitness

Font styles to use
Sans Serif

Colors
3277b5

Requirements
Must have
• Our logo
• Our contact info
• Price
• Call to Action
• List of features and benefits
• Start and end date
• Testimonial or 2
Nice to have
• Here are some testimonials:
• Melinda - Thank you thank you thank you! I went into this hoping to gain awareness of my habitual/stress eating and addiction to sugar and I came out with so much more. I would love to do this again as part of an organized group - please let me know when you do it again! ~Renata B.
• I LOVE this new life style!!! I'm eating foods I would of never thought of.... thank you! ~Gloria M.
• I can't believe I didn't do this sooner! I feel amazing. Down 6 1/2 pounds, skin clearer.....I may not reintroduce certain items (dairy/grains) and feel I don't need it. Thank you for bringing the detox up in the first place, best thing I have done so far. ~Daniela Ortiz
Should not have
• Should not have any pictures of women in sports bras.
• Our clients are "regular" women who dont want to be patronized by the lure of looking like a 20-something fitness model but rather motivated and inspired to do something better for their life.

```html
<!DOCTYPE html>
<html lang="en">
<head>
<meta charset="utf-8">
<title>Motion Harbor 21-Day Detox Flyer</title>
<link rel="stylesheet" href="https://fonts.googleapis.com/css2?family=Oswald:wght@400;500&family=Open+Sans:ital,wght@0,600;0,700;1,400;1,700&display=swap">
<style>
  :root {
    --backdrop: #bcbdbf;
    --yellow: #ffe017;
    --blue: #2459ab;
    --blue-dark: #1d4a93;
    --price-blue: #2a62b5;
    --black: #1b1b1b;
    --white: #ffffff;
    --bullet: #f2a033;
    --photo-wood: #8a6d55;
    --photo-door: #d7c4a2;
    --photo-warm: #6b5a50;
    --photo-beach: #7f9bb0;
  }
  * { box-sizing: border-box; margin: 0; padding: 0; }
  html, body { width: 1200px; height: 1000px; overflow: hidden; }
  body { background: var(--backdrop); font-family: "Open Sans", Arial, sans-serif; position: relative; }
  .flyer { position: absolute; left: 302px; top: 80px; width: 596px; height: 840px; }
  .column-left { position: absolute; left: 0; top: 0; width: 333px; height: 840px; background: var(--yellow); }
  .column-right { position: absolute; left: 333px; top: 0; width: 263px; height: 840px; background: var(--blue); }

  .benefits-band { position: absolute; left: 0; top: 68px; width: 333px; height: 262px; background: var(--black); }
  .benefits-tab { position: absolute; left: 37px; top: 23px; width: 140px; height: 57px; }
  .benefits-tab-title { position: absolute; left: 37px; top: 23px; width: 110px; height: 57px;
    font-family: "Oswald", sans-serif; font-weight: 500; font-size: 25px; color: var(--white);
    line-height: 57px; text-align: center; }
  .benefits-note { position: absolute; left: 156px; top: 71px; font-size: 8.5px; color: var(--white); font-weight: 600; }
  .benefits-list { position: absolute; left: 20px; top: 97px; list-style: none; }
  .benefits-list li { font-size: 11.6px; font-weight: 600; color: var(--white); line-height: 14.4px; white-space: nowrap; }
  .benefits-list li::before { content: "•"; color: var(--bullet); margin-right: 4px; }

  .price-box { position: absolute; left: 27px; width: 266px; background: var(--white); border: 1.5px solid var(--black); padding: 5px 10px; overflow: hidden; }
  .price-box.members { top: 365px; height: 98px; padding-top: 9px; }
  .price-box.guests { top: 490px; height: 98px; }
  .price-line { font-family: "Oswald", sans-serif; font-weight: 400; font-size: 33px; line-height: 40px; color: var(--black); white-space: nowrap; }
  .price-box.members .price-line { font-size: 29px; line-height: 39px; }
  .price-amount { color: var(--price-blue); }
  .price-detail { font-size: 14.5px; line-height: 19px; font-weight: 600; color: var(--black); }

  .register { position: absolute; left: 36px; top: 632px; }
  .register-title { font-family: "Oswald", sans-serif; font-weight: 400; font-size: 42px; line-height: 58px; color: var(--black); }
  .register-info { font-size: 12.4px; font-weight: 700; line-height: 15px; color: var(--black); }

  .brand { position: absolute; left: 35px; top: 748px; display: flex; align-items: center; gap: 10px; }
  .brand-mark { width: 50px; height: 50px; border-radius: 50%; background: var(--black); }
  .brand-name { font-family: "Open Sans", sans-serif; font-weight: 700; font-size: 20px; letter-spacing: 3px; color: var(--black); }

  .photo-grid { position: absolute; left: 29px; top: 32px; width: 205px; height: 205px; background: var(--white);
    display: grid; grid-template-columns: 1fr 1fr; grid-template-rows: 1fr 1fr; gap: 3px; padding: 3px; }
  .photo { width: 100%; height: 100%; }
  .photo.wood { background: linear-gradient(180deg, var(--photo-wood), #6f5643); }
  .photo.door { background: linear-gradient(180deg, var(--photo-door), #bfa985); }

  .testimonials-title { position: absolute; left: 31px; top: 249px; font-family: "Oswald", sans-serif; font-weight: 500;
    font-size: 25px; color: var(--yellow); line-height: 34px; }
  .rule { position: absolute; left: 31px; width: 202px; height: 1px; background: var(--white); }
  .testimonial { position: absolute; left: 32px; width: 200px; font-style: italic; font-size: 10.6px; line-height: 13.2px; color: var(--white); }
  .testimonial cite { display: block; font-weight: 700; font-style: italic; }

  .result-photo { position: absolute; top: 643px; width: 72px; height: 150px; }
  .result-photo.first { left: 58px; background: linear-gradient(180deg, var(--photo-warm), #3e3530); }
  .result-photo.second { left: 140px; background: linear-gradient(180deg, var(--photo-beach), #8d7f6a); }
  .footer-url { position: absolute; left: 0; width: 263px; top: 803px; text-align: center; font-size: 9.5px; font-weight: 700; color: var(--white); }
</style>
</head>
<body>
  <main class="flyer">
    <section class="column-left">
      <svg class="benefits-tab" viewBox="0 0 140 57" aria-hidden="true">
        <polygon points="108,0 140,45 108,45" fill="var(--blue-dark)"/>
        <rect x="0" y="0" width="110" height="57" fill="var(--blue)"/>
      </svg>
      <div class="benefits-band"></div>
      <div class="benefits-tab-title">Benefits</div>
      <p class="benefits-note">(according to past participants)</p>
      <ul class="benefits-list">
        <li>Better Sleep</li>
        <li>Eliminated Hot Flashes</li>
        <li>Got Off Medication (with doctor's supervision)</li>
        <li>Decreased/Eliminated Chronic Pain</li>
        <li>Better Digestion</li>
        <li>Flatter Belly</li>
        <li>Reduced Acne</li>
        <li>Improved Relationships With Food (Less Cravings)</li>
        <li>Enhanced My Relationship With My Spouse</li>
        <li>Never Hungry</li>
        <li>More Energy</li>
        <li>Had Fun Trying New Recipes</li>
        <li>Pants Fell Off</li>
        <li>People Notice More Happiness</li>
        <li>Kids Got Into It And Want To Eat Healthy Now!!!!!</li>
      </ul>

      <div class="price-box members">
        <p class="price-line">Current Motion</p>
        <p class="price-line">Harbor Members <span class="price-amount">$19</span></p>
      </div>
      <div class="price-box guests">
        <p class="price-line">Non-Members <span class="price-amount">$99</span></p>
        <p class="price-detail">Includes Unlimited Fitness<br>in our Group Training Program</p>
      </div>

      <div class="register">
        <h2 class="register-title">Registration at</h2>
        <p class="register-info">www.harborfitstudio.com/21daydetox<br>Or Register By Phone: 707-555-0142</p>
      </div>

      <div class="brand">
        <span class="brand-mark"></span>
        <span class="brand-name">MOTION HARBOR</span>
      </div>
    </section>

    <section class="column-right">
      <div class="photo-grid">
        <div class="photo wood" role="img" aria-label="Participant before the detox, front view against a wooden wall"></div>
        <div class="photo wood" role="img" aria-label="Participant before the detox, side view against a wooden wall"></div>
        <div class="photo door" role="img" aria-label="Participant after the detox, front view in a hallway"></div>
        <div class="photo door" role="img" aria-label="Participant after the detox, side view in a hallway"></div>
      </div>

      <h2 class="testimonials-title">TESTIMONIALS</h2>
      <div class="rule" style="top:284px"></div>

      <blockquote class="testimonial" style="top:298px">
        Melinda – Thank you thank you thank you! I went into this hoping to gain awareness of my habitual/stress eating and addiction to sugar and I came out with so much more. I would love to do this again as part of an organized group – please let me know when you do it again!
        <cite>Renata B.</cite>
      </blockquote>
      <div class="rule" style="top:426px"></div>

      <blockquote class="testimonial" style="top:443px">
        I LOVE this new life style!!! I'm eating foods I would of never thought of.... thank you!
        <cite>Gloria M.</cite>
      </blockquote>
      <div class="rule" style="top:509px"></div>

      <blockquote class="testimonial" style="top:525px">
        “ I can't believe I didn't do this sooner!&nbsp; I feel amazing.&nbsp; Down 6 1/2 pounds, skin clearer.....I may not reintroduce certain items (dairy/grains) and feel I don't need it.&nbsp; Thank you for bringing the detox up in the first place, best thing I have done so far.
        <cite>Daniela Ortiz.</cite>
      </blockquote>

      <div class="result-photo first" role="img" aria-label="Past participant showing her results in a patterned top"></div>
      <div class="result-photo second" role="img" aria-label="Past participant with family at the beach"></div>

      <p class="footer-url">www.harborfitstudio.com</p>
    </section>
  </main>
</body>
</html>
```